UI design needed for a prototype based on wireframe

Hey there.
I need a UI design done on a a prototype application idea before I send it to a programmer. Once designed and programmed the app will move onto a testing faze where it will stay for some time and, I assume, go through several redesign fazes. I have a wireframe mockup and background description so I imagine the design work is pretty straight forward. The app is an activity app that let´s users post different activities that they want to to and post it before a community of users who might be willing to participate. Any features worth mentioning might include Mingleport only log-in, Vantoro routes navigation and star rating system of the user. Besides that I think it´s fairly basic. This app will initially be launched only in vantoro stall because of the test feature of the marketplace.

```html
<!DOCTYPE html>
<html lang="en">
<head>
<meta charset="utf-8">
<title>Activity Profile</title>
<link rel="stylesheet" href="https://fonts.googleapis.com/css2?family=Lato:wght@300;400;700&display=swap">
<style>
  :root {
    --purple: #7b6fd0;
    --purple-light: #9a90e0;
    --white: #ffffff;
    --text-dark: #3a3a3a;
    --text-muted: #a9a9a9;
    --chip-bg: #f1f1f3;
    --chip-text: #a8a8ae;
    --divider: #ececef;
    --star-on: #f5a623;
    --star-off: #d6d6da;
    --page-bg: #f6f6f8;
    --map-green: #cfe2b4;
    --map-grey: #e7e5df;
  }
  * { box-sizing: border-box; margin: 0; padding: 0; }
  html, body { width: 755px; height: 1200px; overflow: hidden; }
  body { font-family: "Lato", sans-serif; background: var(--white); position: relative; }

  .app-header {
    position: absolute; left: 0; top: 0; width: 755px; height: 132px;
    background: linear-gradient(180deg, var(--purple) 0%, var(--purple-light) 100%);
    color: var(--white);
  }
  .status-bar {
    height: 40px; display: flex; align-items: center; justify-content: space-between;
    padding: 0 24px; font-size: 20px; font-weight: 400;
  }
  .status-bar .carrier { display: flex; align-items: center; gap: 8px; }
  .status-bar .time { font-weight: 700; }
  .status-bar .battery { display: flex; align-items: center; gap: 8px; }
  .nav-row { display: flex; align-items: center; height: 92px; padding: 0 36px; gap: 60px; }
  .search-field {
    flex: 1; height: 42px; border: 1px solid rgba(255,255,255,0.55); border-radius: 6px;
    display: flex; align-items: center; justify-content: center; font-size: 19px;
    color: rgba(255,255,255,0.85); font-weight: 300; margin-right: 10px;
  }

  .profile { position: absolute; top: 132px; left: 0; width: 755px; text-align: center; }
  .avatar {
    width: 204px; height: 204px; border-radius: 50%; margin: 54px auto 0;
    border: 6px solid var(--white); box-shadow: 0 2px 10px rgba(0,0,0,0.12);
    background: radial-gradient(circle at 50% 40%, #c9a889 0%, #6b5646 60%, #d7d3cc 100%);
  }
  .profile-name { margin-top: 34px; font-size: 34px; font-weight: 700; letter-spacing: 1px; color: var(--text-dark); }
  .profile-place { margin-top: 6px; font-size: 21px; color: var(--text-muted); font-weight: 300; }

  .rating {
    position: absolute; top: 555px; left: 60px; right: 60px;
    display: flex; align-items: center; justify-content: space-between;
  }
  .stars { display: flex; gap: 8px; }
  .review-count { font-size: 15px; color: var(--text-muted); }

  .divider { position: absolute; top: 635px; left: 0; width: 755px; height: 12px; background: var(--page-bg); }

  .activities { position: absolute; top: 660px; left: 60px; right: 60px; }
  .activities-title { font-size: 23px; font-weight: 700; color: var(--text-dark); margin-bottom: 30px; }
  .activity-grid { display: grid; grid-template-columns: repeat(4, 1fr); column-gap: 45px; row-gap: 34px; }
  .chip {
    height: 42px; border-radius: 3px; background: var(--chip-bg); color: var(--chip-text);
    display: flex; align-items: center; justify-content: center; font-size: 17px;
  }
  .chip.is-selected { background: var(--purple); color: var(--white); }

  .map-area {
    position: absolute; top: 975px; left: 0; width: 755px; height: 225px;
    background: linear-gradient(135deg, var(--map-grey) 0%, var(--map-green) 55%, var(--map-grey) 100%);
  }
</style>
</head>
<body>
  <header class="app-header">
    <div class="status-bar">
      <span class="carrier">
        <svg width="46" height="10" viewBox="0 0 46 10"><g fill="#fff"><circle cx="5" cy="5" r="4"/><circle cx="14" cy="5" r="4"/><circle cx="23" cy="5" r="4"/><circle cx="32" cy="5" r="4"/><circle cx="41" cy="5" r="3.5" fill="none" stroke="#fff"/></g></svg>
        LUMO
        <svg width="20" height="14" viewBox="0 0 20 14"><path d="M10 13 L1 4 A13 13 0 0 1 19 4 Z" fill="#fff"/></svg>
      </span>
      <span class="time">4:21 PM</span>
      <span class="battery">
        <svg width="10" height="16" viewBox="0 0 10 16"><path d="M1 4 L9 12 L5 15 V1 L9 4 L1 12" fill="none" stroke="#fff" stroke-width="1.5"/></svg>
        100%
        <svg width="40" height="18" viewBox="0 0 40 18"><rect x="1" y="1" width="34" height="16" rx="3" fill="#fff"/><rect x="36" y="6" width="3" height="6" rx="1" fill="#fff"/></svg>
      </span>
    </div>
    <div class="nav-row">
      <svg class="menu-icon" width="36" height="26" viewBox="0 0 36 26"><g stroke="#fff" stroke-width="3" stroke-linecap="round"><line x1="2" y1="3" x2="34" y2="3"/><line x1="2" y1="13" x2="34" y2="13"/><line x1="2" y1="23" x2="34" y2="23"/></g></svg>
      <div class="search-field">Search activities</div>
    </div>
  </header>

  <section class="profile">
    <div class="avatar" role="img" aria-label="Profile photo of the user"></div>
    <h1 class="profile-name">ARLEN VOSS</h1>
    <p class="profile-place">Elmsvik, Norda</p>
  </section>

  <div class="rating">
    <div class="stars">
      <svg width="192" height="34" viewBox="0 0 192 34">
        <defs><path id="star" d="M17 1 L21.7 11.6 L33 12.6 L24.4 20.2 L27 31.5 L17 25.6 L7 31.5 L9.6 20.2 L1 12.6 L12.3 11.6 Z"/></defs>
        <use href="#star" x="0" fill="var(--star-on)"/>
        <use href="#star" x="39" fill="var(--star-on)"/>
        <use href="#star" x="78" fill="var(--star-on)"/>
        <use href="#star" x="117" fill="var(--star-on)"/>
        <use href="#star" x="156" fill="var(--star-off)"/>
      </svg>
    </div>
    <span class="review-count">Based on 11 reviews</span>
  </div>

  <div class="divider"></div>

  <section class="activities">
    <h2 class="activities-title">Activities</h2>
    <div class="activity-grid">
      <span class="chip">Movies</span>
      <span class="chip">Running</span>
      <span class="chip is-selected">Museums</span>
      <span class="chip">Clubs</span>
      <span class="chip is-selected">Movies</span>
      <span class="chip">Running</span>
      <span class="chip">Museums</span>
      <span class="chip is-selected">Clubs</span>
      <span class="chip">Movies</span>
      <span class="chip">Running</span>
      <span class="chip">Museums</span>
      <span class="chip">Clubs</span>
    </div>
  </section>

  <div class="map-area" role="img" aria-label="Street map with pins marking nearby activity locations"></div>
</body>
</html>
```